Business Card & Letterhead Design

We a financial advice company based in Australia. We provide advice to wealthy farmers.

We are changing our business name FROM Brightmere Financial TO Calderstone Wealth and we need a new letterhead and double sided business card design

Attached is designs from our previous branding (Brightmere Financial) as it includes all the details we require on the new Calderstone Wealth business cards and letterhead.

```html
<!DOCTYPE html>
<html lang="en">
<head>
<meta charset="utf-8">
<title>Calderstone Wealth – Business Card</title>
<link rel="stylesheet" href="https://fonts.googleapis.com/css2?family=Montserrat:wght@400;500;600;700&display=swap">
<style>
  :root {
    --page: #e6e3df;
    --card: #333335;
    --card-edge: #f2f2f2;
    --ink: #ffffff;
    --ink-soft: #d9d9d9;
    --emboss: #56575a;
    --emboss-light: #8a8b8e;
  }
  * { box-sizing: border-box; margin: 0; padding: 0; }
  html, body { width: 1200px; height: 800px; overflow: hidden; }
  body {
    background: var(--page);
    font-family: "Montserrat", Arial, sans-serif;
    color: var(--ink);
    display: flex;
    align-items: center;
    justify-content: center;
    gap: 40px;
  }
  .card {
    position: relative;
    width: 560px;
    height: 320px;
    background: var(--card);
    border: 2px solid var(--card-edge);
    box-shadow: 0 10px 24px rgba(0,0,0,.25);
  }

  /* Back side */
  .card-back {
    display: flex;
    flex-direction: column;
    align-items: center;
    justify-content: center;
    text-align: center;
    color: var(--ink-soft);
  }
  .brand-mark {
    width: 46px; height: 46px;
    border: 2px solid currentColor;
    border-radius: 50%;
    margin-bottom: 8px;
  }
  .card-back .brand-mark { color: var(--emboss-light); }
  .brand-name {
    font-weight: 500;
    letter-spacing: 1px;
    text-transform: uppercase;
  }
  .card-back .brand-name { font-size: 22px; color: var(--emboss-light); }
  .brand-tagline {
    font-size: 9px;
    letter-spacing: 2.6px;
    text-transform: uppercase;
    margin-top: 2px;
  }
  .card-back .brand-tagline { color: var(--emboss); margin-bottom: 18px; }
  .services, .licensee { font-size: 12px; line-height: 1.35; }
  .licensee { margin-top: 16px; }

  /* Front side */
  .card-front { display: flex; }
  .front-brand {
    width: 290px;
    display: flex;
    flex-direction: column;
    align-items: center;
    padding-top: 58px;
  }
  .front-brand .brand-name { font-size: 20px; }
  .front-brand .brand-tagline { color: var(--ink-soft); font-size: 8.5px; }
  .motto { font-weight: 700; font-size: 13px; margin-top: 12px; letter-spacing: .3px; }
  .referral {
    position: absolute;
    left: 0; width: 290px;
    bottom: 30px;
    text-align: center;
    font-size: 12px;
    letter-spacing: .5px;
  }
  .divider {
    position: absolute;
    left: 290px; top: 40px; bottom: 60px;
    width: 1px; background: var(--ink);
  }
  .contact { padding: 42px 0 0 18px; font-size: 12px; line-height: 1.3; }
  .person-name { font-weight: 700; font-size: 16px; }
  .credentials { font-size: 11px; font-weight: 400; }
  .role { margin-bottom: 6px; }
  .contact-list { list-style: none; }
  .contact-list li { display: flex; align-items: center; gap: 6px; }
  .contact-list svg { width: 11px; height: 11px; flex: none; }
  .address { margin-top: 10px; }
</style>
</head>
<body>

  <section class="card card-back" aria-label="Business card back">
    <div class="brand-mark" aria-hidden="true"></div>
    <div class="brand-name">Calderstone Wealth</div>
    <div class="brand-tagline">Strategic Financial Advice</div>
    <p class="services">Personal &amp; Business Insurance Solutions<br>Business Estate Planning<br>Succession Planning</p>
    <p class="licensee">Meridian Advice Partners Limited<br>Australian Financial Services Licensee License Number 500123</p>
  </section>

  <section class="card card-front" aria-label="Business card front">
    <div class="front-brand">
      <div class="brand-mark" aria-hidden="true"></div>
      <div class="brand-name">Calderstone Wealth</div>
      <div class="brand-tagline">Strategic Financial Advice</div>
      <p class="motto">'Financial peace of mind'</p>
    </div>
    <p class="referral">A referral built business</p>
    <div class="divider"></div>
    <div class="contact">
      <p class="person-name">Sam Hollis <span class="credentials">B.Com. Dip F.P. Adv Dip FS</span></p>
      <p>Managing Director</p>
      <p class="role">Authorised Representative</p>
      <ul class="contact-list">
        <li><svg viewBox="0 0 12 12" fill="#fff"><path d="M2 1h2.5l1 3-1.5 1a6 6 0 0 0 3 3l1-1.5 3 1V11c-5 .5-9.5-4-9-9z"/></svg>(07) 3000 1452</li>
        <li><svg viewBox="0 0 12 12" fill="#fff"><rect x="3" y="1" width="6" height="3"/><rect x="1" y="4.5" width="10" height="5" rx="1"/><rect x="3" y="8" width="6" height="3" fill="#333335" stroke="#fff"/></svg>(07) 3000 1453</li>
        <li><svg viewBox="0 0 12 12" fill="none" stroke="#fff" stroke-width="1.4"><rect x="3.5" y="1" width="5" height="10" rx="1"/></svg>0400 118 236</li>
        <li><svg viewBox="0 0 12 12" fill="none" stroke="#fff" stroke-width="1.2"><rect x="1" y="2.5" width="10" height="7"/><path d="M1 2.5l5 4 5-4"/></svg>sam@brightmerefinancial.com.au</li>
        <li><svg viewBox="0 0 12 12" fill="none" stroke="#fff" stroke-width="1.1"><circle cx="6" cy="6" r="5"/><ellipse cx="6" cy="6" rx="2.2" ry="5"/><path d="M1 6h10"/></svg>www.brightmerefinancial.com.au</li>
      </ul>
      <p class="address">Suite 4A, 17 Wexley St<br>Riverbend QLD 4100<br>PO Box 5120, Riverbend QLD 4100</p>
    </div>
  </section>

</body>
</html>
```